Flyer Design sales and lettings

We need a double sided flyer for our Estate and Letting agency. We have just moved in to 16th century office and expanded our offer to commercial and residential sales (previously we were targeted on lettings only). We are based in small rural town in Midlands, UK.Any photos, graphics will need to be linked to our location (please dont use skyscrapers :)One side of our flyer will have to treat about lettings and our offer - 7% plus vat commission on all new lettings, no extra costs, rent guarantee insurance, we are open 6 days a week and available 24/7.Please insert information about our commercial department on this side as well. "Landlords! Did you know that we also do commercial lettings? Call us on 01427918305 for best offer in the area. Other side informing clients about our sales offer 0.7% plus vat on all new sales instructions, free market appraisal, no up front costs, no sale no fee, we are open 6 days a week and available 24/7Here is our website: www.morvenhomesteads.uk We are members of KTV, BLW and leasewell9 (logos attached)Thank you Tomasz Wielgorek
Updates

Target Market(s)

Landlords and vendors in local area

Industry/Entity Type

Real Estate Agent

Font styles to use
Decorative
Script

Requirements
Must have
• all points stated in descriptip
Nice to have
• our logo or parts of it incorporated in design, elegant retro, stylish effcts.
• Silver/Charcoal coulour with retro gold theme.
Should not have
• modern, city accents.

```html
<!DOCTYPE html>
<html lang="en">
<head>
<meta charset="utf-8">
<title>Morven Homesteads – Lettings &amp; Sales Flyer</title>
<link rel="stylesheet" href="https://fonts.googleapis.com/css2?family=Sorts+Mill+Goudy:ital@0;1&display=swap">
<style>
:root{
  --page:#ecebe8;
  --paper:#f4f3f1;
  --charcoal:#6f6b6d;
  --charcoal-dark:#3d3a3b;
  --silver:#cfcdcc;
  --silver-light:#e6e5e3;
  --gold:#c9b46a;
  --gold-light:#efe6bd;
  --ink:#4a4647;
  --white:#ffffff;
}
*{box-sizing:border-box;margin:0;padding:0}
html,body{width:1200px;height:1200px;overflow:hidden}
body{background:var(--page);font-family:"Sorts Mill Goudy",Georgia,serif;color:var(--ink);position:relative}
.flyer{position:absolute;top:232px;width:520px;height:736px;background:var(--paper);box-shadow:0 6px 18px rgba(0,0,0,.18);overflow:hidden}
.flyer--lettings{left:50px}
.flyer--sales{left:630px}

/* brand block */
.brand{position:absolute;background:var(--charcoal);color:var(--white);padding:14px 20px;text-align:center;line-height:1.05;border:2px solid var(--silver-light);outline:1px solid var(--charcoal)}
.brand__name{font-size:30px}
.brand__name span{display:block}

/* photo placeholders */
.photo{position:absolute;left:0;width:100%}
.photo--garden{top:0;height:200px;background:linear-gradient(135deg,#5f6f3c,#8a7a5c 45%,#b8b2a6 75%,#6d7a45)}
.photo--terrace{top:0;height:215px;background:linear-gradient(120deg,#8d8b89,#c9c7c4 50%,#9d9b98)}
.photo--building{left:24px;top:430px;width:200px;height:185px;background:linear-gradient(180deg,#cbc3b8,#9d9288 60%,#e1ddd8)}

/* lettings side */
.flyer--lettings .brand{left:30px;top:36px}
.band{position:absolute;left:0;top:200px;width:100%;height:120px;background:var(--charcoal);color:var(--white)}
.rate{position:absolute;font-size:120px;line-height:1;letter-spacing:-4px}
.rate sup{font-size:54px;vertical-align:top;position:relative;top:8px}
.band .rate{left:20px;top:10px}
.offer{position:absolute;left:160px;top:20px;font-size:19px;line-height:1.35}
.offer strong{font-weight:400;font-size:21px}
.lead{position:absolute;left:24px;top:336px;width:480px;font-size:30px;line-height:1.15;color:var(--charcoal-dark)}
.lead em{font-size:20px}
.about{position:absolute;left:240px;top:424px;width:260px;font-size:12.5px;line-height:1.3;color:var(--charcoal-dark)}
.about b{font-weight:400;font-size:14px}
.contact{position:absolute;left:0;bottom:0;width:100%;padding:0 24px}
.contact__line{font-size:30px;color:var(--charcoal);white-space:nowrap}
.contact__web{font-size:20px}
.contact__address{font-size:13.5px;color:var(--charcoal);margin-top:4px;white-space:nowrap}
.flyer--lettings .contact{top:630px;padding-top:18px;background:linear-gradient(180deg,rgba(244,243,241,0),#b9b6b5)}

/* sales side */
.flyer--sales .brand{right:26px;top:20px}
.sales-rate{position:absolute;left:22px;top:230px;color:var(--charcoal)}
.sales-rate .rate{position:static;font-size:96px}
.sales-offer{position:absolute;left:215px;top:250px;width:290px;font-size:17px;line-height:1.35;color:var(--charcoal-dark)}
.services{position:absolute;left:0;top:350px;width:100%;height:230px;background:linear-gradient(180deg,var(--gold-light),var(--gold) 55%,var(--gold-light))}
.services svg{position:absolute;left:0;top:0}
.partners{position:absolute;left:0;top:600px;width:100%;display:flex;justify-content:space-around;align-items:center;padding:0 20px}
.partner{display:flex;align-items:center;gap:6px;font-size:20px;color:var(--charcoal-dark)}
.partner::before{content:"";width:12px;height:12px;background:var(--charcoal)}
.flyer--sales .contact{top:650px;padding-top:0}
.flyer--sales .contact__line{font-size:27px}
.flyer--sales .contact__web{font-size:18px}
.flyer--sales .contact__address{font-size:13.5px}
</style>
</head>
<body>

<section class="flyer flyer--lettings" aria-label="Lettings side">
  <div class="photo photo--garden" role="img" aria-label="Photograph of a cottage courtyard garden with planter, flowers and a table set with red wine"></div>
  <div class="brand">
    <div class="brand__name"><span>Morven</span><span>Homesteads</span></div>
  </div>
  <div class="band">
    <div class="rate">7<sup>%</sup></div>
    <p class="offer">plus VAT commission on <strong>all new lettings.</strong><br>No extra costs, rent guarantee insurance.<br>Open 6 days a week and available 24/7.</p>
  </div>
  <p class="lead">Landlords! <em>Did you know that we also do commercial lettings? Call us today for best offer in the area.</em></p>
  <div class="photo photo--building" role="img" aria-label="Sepia photograph of a Georgian brick town house"></div>
  <p class="about"><b>We are a unique property company offering a professional service whilst adopting a personal approach.</b> Our services can be tailored to handle your requirements in every aspect of the property market. Lettings, Residential &amp; Commercial, Investment and Management. With an extensive knowledge of the property market we are dedicated to finding the perfect property solution for investors, tenants, landlords, buyers and sellers alike.</p>
  <div class="contact">
    <p class="contact__line">01427-918-305 <span class="contact__web">www.morvenhomesteads.uk</span></p>
    <p class="contact__address">Ashcombe House, 27 Market Street, Pershore, WR10 2HL, United Kingdom</p>
  </div>
</section>

<section class="flyer flyer--sales" aria-label="Sales side">
  <div class="photo photo--terrace" role="img" aria-label="Greyscale photograph of a row of Victorian terraced houses with bay windows"></div>
  <div class="brand">
    <div class="brand__name"><span>Morven</span><span>Homesteads</span></div>
  </div>
  <div class="sales-rate"><div class="rate">0.7<sup>%</sup></div></div>
  <p class="sales-offer">plus VAT on all new sales instructions, free market appraisal, no up front costs, no sale no fee, we are open 6 days a week and available 24/7</p>
  <div class="services">
    <svg width="520" height="230" viewBox="0 0 520 230" font-family="Sorts Mill Goudy, Georgia, serif" fill="#4a4647">
      <g stroke="#5a5556" stroke-width="1.2" fill="none">
        <line x1="30" y1="140" x2="130" y2="140"/>
        <rect x="130" y="122" width="86" height="36"/>
        <line x1="216" y1="140" x2="232" y2="140"/>
        <rect x="232" y="110" width="60" height="30"/>
        <line x1="292" y1="125" x2="306" y2="125"/>
        <rect x="306" y="100" width="86" height="32"/>
        <line x1="392" y1="116" x2="410" y2="116"/>
        <rect x="410" y="74" width="96" height="32"/>
      </g>
      <text x="260" y="60" font-size="22" text-anchor="middle">Morven Homesteads</text>
      <text x="173" y="145" font-size="13" text-anchor="middle">Lettings</text>
      <text x="262" y="129" font-size="12" text-anchor="middle">Sales</text>
      <text x="349" y="120" font-size="12" text-anchor="middle">Residential</text>
      <text x="458" y="95" font-size="13" text-anchor="middle">Commercial</text>
    </svg>
  </div>
  <div class="partners">
    <span class="partner">BLW</span>
    <span class="partner">KTV</span>
    <span class="partner">Homevista</span>
    <span class="partner">leasewell9</span>
  </div>
  <div class="contact">
    <p class="contact__line">01427-918-305 <span class="contact__web">www.morvenhomesteads.uk</span></p>
    <p class="contact__address">Ashcombe House, 27 Market Street, Pershore, WR10 2HL, United Kingdom</p>
  </div>
</section>

</body>
</html>
```